Friendly website/webshop needed for small family store

Hello .. I really need a website that is easy to use as I have no experience with this at all. ..
My shop is called sandpiper and I had a fantastic logo from pixel guild - I asked for something mid century modern and I love it. I will attach . There might be some development around the logo now for various paraphernalia ( stickers , printed tissue paper carrier bags etc.. ) I would also like some sort of help with a slogan such as 'sing your prettiest song' as in,  live your best life etc..  but I'm not sure if this is a little trite .... ? but it would be nice to link the sandpiper with a little Motto.    If I need to pay extra for this - please could you let me know ... I'm happy to add on payment ..
As you can see the only LOGO colours really are grey black and orange .. so I would like some ideas to expand on the bird  to bring in some more colours.....  the tag line flower.children.home I would like to drop..
* the original brief included flowers on the tag line  because at the time we were also a florist . we now just sell dried flowers
My shop is in the beautiful town of Malvern, we have lots of tourist that come to walk the hills and enjoy nature - it's a family and dog friendly sort of town and we are a dog and family friendly sort of shop :-) It's a relaxed space that focuses on beautiful handmade items such as baskets & wooden utensils  from Africa, textiles from India and ceramics from France, Portugal and Italy.  We have a lovely section for children that sells beautiful soft toys from Tavel Brune and the wonderful mice family and bunnies from Osvika.
We stock TAMBO homeware which is lovely and earthy and natural.
We would like to communicate the value of buying thoughtfully  and conscientiously, of building a beautiful home whilst investing in & supporting makers world wide. We don't sell anything that can't be repurposed, recycled etc..
Thank you

```html
<!DOCTYPE html>
<html lang="en">
<head>
<meta charset="utf-8">
<title>Sandpiper – Home</title>
<link href="https://fonts.googleapis.com/css2?family=Outfit:wght@300;400;500;600&family=Bowlby+One&display=swap" rel="stylesheet">
<style>
:root{
  --ink:#1d1d1d;
  --muted:#555;
  --accent:#d9826b;
  --teal:#6eaabb;
  --teal-band:#79b1c2;
  --panel:#eeeeee;
  --footer-bottom:#e2e2e2;
  --star:#f2b705;
  --white:#ffffff;
}
*{margin:0;padding:0;box-sizing:border-box}
html,body{width:1200px;height:4491px;overflow:hidden}
body{font-family:"Outfit",sans-serif;color:var(--ink);background:var(--white);position:relative}
.abs{position:absolute}
.ph{position:absolute}

/* header */
.site-header{top:0;left:0;width:1200px;height:132px;background:var(--white);border-top:2px solid var(--accent)}
.brand{left:98px;top:74px;font-size:30px;font-weight:600;color:#333;letter-spacing:.5px;display:flex;align-items:center;gap:8px;line-height:1}
.brand .dot{width:14px;height:14px;border-radius:50%;background:var(--accent)}
.search{left:505px;top:22px;width:480px;height:40px;border:1px solid #ccc;border-radius:20px;font-size:12px;color:#444;padding:12px 0 0 22px;line-height:1}
.search-btn{left:948px;top:26px;width:32px;height:32px;border-radius:50%;background:var(--accent)}
.nav{position:absolute;top:92px;left:0;width:1200px;height:20px;font-size:14px;font-weight:500;color:var(--ink)}
.nav span{position:absolute;top:0;white-space:nowrap;line-height:1}
.nav .active{color:var(--accent)}

/* hero */
.hero{top:132px;left:0;width:1200px;height:626px;background:linear-gradient(135deg,#6a6c6a 0%,#c9c6bd 45%,#9c8f78 75%,#5b5750 100%)}
.hero-title{left:98px;top:350px;font-family:"Bowlby One",sans-serif;font-size:58px;color:var(--white);line-height:1}
.hero-copy{left:100px;top:418px;font-size:15px;color:var(--white);line-height:26px}
.btn{position:absolute;background:var(--teal);color:var(--white);border-radius:22px;font-size:13px;font-weight:600;text-align:center;line-height:1}
.dots span{position:absolute;width:11px;height:11px;border-radius:50%;border:1.5px solid var(--white)}

/* sections */
.section-title{position:absolute;left:0;width:1200px;text-align:center;font-size:40px;font-weight:500;line-height:1.2}
.panel{left:0;width:1200px;background:var(--panel)}
.card{position:absolute;background:var(--white);border:1px solid #ddd;box-shadow:3px 3px 0 #e6e6e6}
.card .label{position:absolute;left:0;width:100%;text-align:center;font-size:20px;font-weight:600}
.prod-name{position:absolute;left:0;width:100%;text-align:center;font-size:11.5px;font-weight:500}
.stars{position:absolute;color:var(--star);font-size:11px;letter-spacing:1px}
.price{position:absolute;left:0;width:100%;text-align:center;font-size:13px}

.about-photo{top:1863px;left:0;width:1200px;height:564px;background:linear-gradient(120deg,#5f93a0 0%,#8aa06a 35%,#566b3a 60%,#7d7e6e 100%)}
.about-box{left:664px;top:1958px;width:437px;height:374px;background:var(--white);padding:24px 26px}
.about-box h2{font-size:40px;font-weight:500;margin-bottom:14px;line-height:1.2}
.about-box p{font-size:13.5px;line-height:26px;color:#444;margin-bottom:10px}

.review{position:absolute;width:315px}
.quote{width:44px;height:44px;border-radius:50%;background:var(--accent);display:flex;align-items:center;justify-content:center;color:var(--white);font-size:34px;font-weight:600;line-height:1;padding-top:14px}
.review h3{font-size:16.5px;font-weight:500;margin:8px 0 4px}
.review p{font-size:13.5px;font-style:italic;color:#555;line-height:26.5px}

.newsletter{top:2917px;left:0;width:1200px;height:306px;background:var(--teal-band);color:var(--white);text-align:center}
.newsletter h2{position:absolute;top:72px;width:100%;font-size:44px;font-weight:400}
.newsletter p{position:absolute;top:140px;width:100%;font-size:14px}
.nl-input{left:303px;top:185px;width:594px;height:38px;background:var(--white);border-radius:20px;color:#333;font-size:12px;text-align:left;padding:13px 0 0 22px;line-height:1}
.nl-btn{left:743px;top:187px;width:152px;height:34px;border-radius:18px;background:var(--accent);font-size:13px;font-weight:600;padding-top:11px;line-height:1}

.blog h3{position:absolute;left:12px;top:240px;width:282px;font-size:16px;font-weight:500;line-height:22px}
.blog p{position:absolute;left:12px;top:294px;width:282px;font-size:13.5px;color:#444;line-height:26.5px;text-align:justify}

.footer{top:4160px;left:0;width:1200px;height:268px;background:var(--panel)}
.footer h4{position:absolute;font-size:15px;font-weight:500}
.footer a{position:absolute;font-size:13px;color:#333;text-decoration:none}
.pay{position:absolute;width:48px;height:28px;border-radius:3px;background:#c9d3e0}
.social{position:absolute;width:36px;height:36px;border-radius:50%;border:1.5px solid #222}
.copy{left:0;top:4428px;width:1200px;height:63px;background:var(--footer-bottom);font-size:12.5px;color:#444;text-align:center;padding-top:22px}
</style>
</head>
<body>

<header class="abs site-header">
  <div class="abs brand"><span class="dot"></span>sandpiper</div>
  <div class="abs search">What are you looking for?</div>
  <div class="abs search-btn"></div>
  <svg class="abs" style="left:1005px;top:30px" width="100" height="24" viewBox="0 0 100 24" fill="none" stroke="#222" stroke-width="1.6">
    <path d="M11 20 L3 12 A4.5 4.5 0 0 1 11 6 A4.5 4.5 0 0 1 19 12 Z"/>
    <circle cx="45" cy="8" r="4.5"/><path d="M37 21 C37 14 53 14 53 21"/>
    <path d="M73 9 H89 L87 21 H75 Z"/><path d="M77 9 V6 A4 4 0 0 1 85 6 V9"/>
    <circle cx="90" cy="18" r="4.5" fill="#fff"/>
  </svg>
  <nav class="nav">
    <span class="active" style="left:343px">HOME</span>
    <span style="left:442px">SHOP</span>
    <span style="left:535px">FLOWERS</span>
    <span style="left:659px">CHILDERN</span>
    <span style="left:789px">GIFTS</span>
    <span style="left:883px">ABOUT US</span>
    <span style="left:1011px">CONACT US</span>
  </nav>
</header>

<section class="ph hero" role="img" aria-label="Shop front with large windows, baskets, wicker chairs and potted plants on the pavement"></section>
<h1 class="abs hero-title">Sandpiper</h1>
<p class="abs hero-copy">Lorem ipsum dolor sit amet, consectetur adipiscing elit,<br>sed do eiusmod tempor incididunt ut labore</p>
<a class="btn" style="left:100px;top:493px;width:160px;height:42px;padding-top:15px">SHOP NOW ➜</a>
<svg class="abs" style="left:50px;top:425px" width="1110" height="40" fill="none" stroke="#fff" stroke-width="1.5"><path d="M18 4 L4 20 L18 36"/><path d="M1092 4 L1106 20 L1092 36"/></svg>
<div class="dots">
  <span style="left:556px;top:712px"></span><span style="left:581px;top:712px;background:#fff"></span>
  <span style="left:606px;top:712px"></span><span style="left:631px;top:712px"></span>
</div>

<section class="abs panel" style="top:758px;height:538px"></section>
<h2 class="section-title" style="top:820px">Product Category</h2>
<div class="card" style="left:105px;top:900px;width:305px;height:318px">
  <div class="ph" style="left:10px;top:10px;width:285px;height:247px;background:linear-gradient(135deg,#4d6b3a,#c7652f,#8b6f52)" role="img" aria-label="Potted plants and dried flowers on shop shelves"></div>
  <div class="label" style="top:275px">FLOWERS</div></div>
<div class="card" style="left:447px;top:900px;width:305px;height:318px">
  <div class="ph" style="left:10px;top:10px;width:285px;height:247px;background:linear-gradient(135deg,#8c7150,#d9c7a8,#b55a78)" role="img" aria-label="Soft toy mice and bunnies in a wicker basket"></div>
  <div class="label" style="top:275px">CHILDERN</div></div>
<div class="card" style="left:788px;top:900px;width:305px;height:318px">
  <div class="ph" style="left:10px;top:10px;width:285px;height:247px;background:linear-gradient(135deg,#5e4a3a,#c5a888,#7d6550)" role="img" aria-label="Shop interior with baskets, ceramics and homeware"></div>
  <div class="label" style="top:275px">GIFTS</div></div>

<h2 class="section-title" style="top:1355px">New Arrivals</h2>
<div class="card" style="left:103px;top:1430px;width:237px;height:283px">
  <div class="ph" style="left:8px;top:8px;width:219px;height:184px;background:linear-gradient(160deg,#5b7c92,#e4a4b0,#d8d2c6)" role="img" aria-label="Tulips in a woven bag"></div>
  <div class="prod-name" style="top:207px">FINIBUS BONORUM ET MAL</div><div class="stars" style="left:92px;top:228px">★★★★★</div><div class="price" style="top:252px">$34.00</div></div>
<div class="card" style="left:356px;top:1430px;width:237px;height:283px">
  <div class="ph" style="left:8px;top:8px;width:219px;height:184px;background:linear-gradient(160deg,#c9a257,#a0785a,#dcd2c2)" role="img" aria-label="Wooden vases and bowl"></div>
  <div class="prod-name" style="top:207px">FINIBUS BONORUM ET MAL</div><div class="stars" style="left:92px;top:228px">★★★★★</div><div class="price" style="top:252px">$34.00</div></div>
<div class="card" style="left:608px;top:1430px;width:237px;height:283px">
  <div class="ph" style="left:8px;top:8px;width:219px;height:184px;background:linear-gradient(160deg,#1e2a3a,#3f7f95,#cbc6bf)" role="img" aria-label="Children's books and soft toy on a shelf"></div>
  <div class="prod-name" style="top:207px">FINIBUS BONORUM ET MAL</div><div class="stars" style="left:92px;top:228px">★★★★★</div><div class="price" style="top:252px">$34.00</div></div>
<div class="card" style="left:862px;top:1430px;width:237px;height:283px">
  <div class="ph" style="left:8px;top:8px;width:219px;height:184px;background:linear-gradient(160deg,#e6e4e0,#a08a5e,#d9d6d0)" role="img" aria-label="Dried flowers in a woven basket"></div>
  <div class="prod-name" style="top:207px">FINIBUS BONORUM ET MAL</div><div class="stars" style="left:92px;top:228px">★★★★★</div><div class="price" style="top:252px">$34.00</div></div>
<a class="btn" style="left:497px;top:1751px;width:206px;height:40px;padding-top:14px">MORE PRODUCTS ➜</a>

<section class="ph about-photo" role="img" aria-label="Straw basket with a pink towel and beach toys on a grassy clifftop by the sea"></section>
<div class="abs about-box">
  <h2>About Us</h2>
  <p>Sed ut perspiciatis unde te natus error sit voluptatem accusantium doloremque , totam rem aperiam, eaque ipsa quae ab illo inventore veritatis et quasi architecto beatae vitae dicta sunt explicabo.</p>
  <p>Sed ut perspiciatis unde te natus error sit voluptatem accusantium doloremque , totam rem aperiam, eaque ipsa quae ab illo inventore</p>
</div>
<a class="btn" style="left:690px;top:2258px;width:160px;height:40px;padding-top:14px">LEARN MORE ➜</a>

<h2 class="section-title" style="top:2517px">Reviews From Our Customers</h2>
<svg class="abs" style="left:50px;top:2715px" width="1110" height="44" fill="none" stroke="#222" stroke-width="1.5"><path d="M18 4 L4 22 L18 40"/><path d="M1092 4 L1106 22 L1092 40"/></svg>
<div class="review" style="left:101px;top:2615px"><div class="quote">“</div><div class="stars" style="position:static;margin-top:12px">★★★★★</div><h3>THE STANDARD LOREM IPSUM PASS</h3><p>Sed ut perspiciatis unde te natus error sit voluptatem accusanum doloremque , totam rem aperiam, eaque</p></div>
<div class="review" style="left:446px;top:2615px"><div class="quote">“</div><div class="stars" style="position:static;margin-top:12px">★★★★★</div><h3>THE STANDARD LOREM IPSUM PASS</h3><p>Sed ut perspiciatis unde te natus error sit voluptatem accusanum doloremque , totam rem aperiam, eaque</p></div>
<div class="review" style="left:791px;top:2615px"><div class="quote">“</div><div class="stars" style="position:static;margin-top:12px">★★★★★</div><h3>THE STANDARD LOREM IPSUM PASS</h3><p>Sed ut perspiciatis unde te natus error sit voluptatem accusanum doloremque , totam rem aperiam, eaque</p></div>

<section class="abs newsletter">
  <h2>Subscribe To The Newsletter</h2>
  <p>Subscribe to our newsletter to stay up to date with the latest news and offers.</p>
  <div class="abs nl-input">Enter your email address</div>
  <div class="abs nl-btn">SUBSCRIBE ➜</div>
</section>

<h2 class="section-title" style="top:3295px">Latest Blog</h2>
<div class="card blog" style="left:105px;top:3373px;width:307px;height:390px">
  <div class="ph" style="left:10px;top:12px;width:287px;height:206px;background:linear-gradient(135deg,#efe8e2,#d4a8b6,#b89d72)" role="img" aria-label="Dried flowers in a woven basket"></div>
  <h3>The standard Lorem Ipsum passa ge, used since the 1500s</h3><p>Sed ut perspiciatis unde te natus error sit voluptataccusantium doloremque , totam rem aperiam</p></div>
<div class="card blog" style="left:447px;top:3373px;width:307px;height:390px">
  <div class="ph" style="left:10px;top:12px;width:287px;height:206px;background:linear-gradient(135deg,#e8e2d8,#b9a994,#f1ede6)" role="img" aria-label="Book and ceramic vases on a table"></div>
  <h3>The standard Lorem Ipsum passa ge, used since the 1500s</h3><p>Sed ut perspiciatis unde te natus error sit voluptataccusantium doloremque , totam rem aperiam</p></div>
<div class="card blog" style="left:788px;top:3373px;width:307px;height:390px">
  <div class="ph" style="left:10px;top:12px;width:287px;height:206px;background:linear-gradient(135deg,#8b6245,#5a3d2c,#a57c5c)" role="img" aria-label="Turned wooden vessel"></div>
  <h3>The standard Lorem Ipsum passa ge, used since the 1500s</h3><p>Sed ut perspiciatis unde te natus error sit voluptataccusantium doloremque , totam rem aperiam</p></div>

<h2 class="section-title" style="top:3842px">Follow On Instagram</h2>
<div class="ph" style="left:0;top:3923px;width:230px;height:221px;background:linear-gradient(135deg,#9ab0c4,#23283a,#c9b89a)" role="img" aria-label="Dark ceramic jugs"></div>
<div class="ph" style="left:242px;top:3923px;width:230px;height:221px;background:linear-gradient(135deg,#3d5a2a,#d8a34a,#c47a4a)" role="img" aria-label="Soft toy bear with honey jars and eggs"></div>
<div class="ph" style="left:485px;top:3923px;width:230px;height:221px;background:linear-gradient(135deg,#f0ece6,#5d8a4a,#c8a67a)" role="img" aria-label="Cactus in a raffia pot"></div>
<div class="ph" style="left:727px;top:3923px;width:230px;height:221px;background:linear-gradient(135deg,#eeeae4,#d88aa0,#7fb8c0)" role="img" aria-label="Baskets with pompoms hanging on a wall"></div>
<div class="ph" style="left:970px;top:3923px;width:230px;height:221px;background:linear-gradient(135deg,#e8d85a,#b9653a,#7c8f55)" role="img" aria-label="Daffodils in terracotta pots"></div>

<footer class="abs footer">
  <div class="abs" style="left:100px;top:150px;display:flex;align-items:center;gap:10px;font-size:38px;font-weight:600;color:#333;line-height:1"><span style="width:18px;height:18px;border-radius:50%;background:var(--accent)"></span>sandpiper</div>
  <h4 style="left:355px;top:53px">QUICK LINKS</h4>
  <a style="left:355px;top:88px">Home</a><a style="left:355px;top:118px">About</a><a style="left:355px;top:148px">Prouct</a><a style="left:355px;top:178px">Blog</a><a style="left:355px;top:208px">Contact</a>
  <h4 style="left:519px;top:53px">HELP</h4>
  <a style="left:519px;top:88px">Faq</a><a style="left:519px;top:118px">Shipping &amp; returns</a><a style="left:519px;top:148px">Contact us</a><a style="left:519px;top:178px">Accessibility</a>
  <h4 style="left:700px;top:53px">OTHERS</h4>
  <a style="left:700px;top:88px">Terms &amp; conditions</a><a style="left:700px;top:118px">Privacy policy</a><a style="left:700px;top:148px">Site map</a>
  <h4 style="left:885px;top:53px">CONTACT</h4>
  <a style="left:885px;top:88px">01632 960418</a><a style="left:885px;top:118px">hello@sandpiper-shop.com</a>
  <span class="pay" style="left:885px;top:148px"></span><span class="pay" style="left:942px;top:148px"></span><span class="pay" style="left:999px;top:148px"></span><span class="pay" style="left:1056px;top:148px"></span>
  <span class="social" style="left:885px;top:198px"></span><span class="social" style="left:931px;top:198px"></span><span class="social" style="left:977px;top:198px"></span><span class="social" style="left:1023px;top:198px"></span>
</footer>
<div class="abs copy">©Copyright ©2024 Sandpiper UK&nbsp; All Rights Reserved.</div>

</body>
</html>
```